Machinery Instruction Manual

We need an instruction manual design that will be used as a template for all user manuals for our range of consumer machinery.
Our product range includes Chainsaws and Jackhammers for example.
======================
Essential:
======================
A staff member with only *Basic* Microsoft Word skills must be able to paste the required content from external sources in to the template to produce a professional manual.
The document should use the minimum amount of automated features.
Our staff need to produce manuals without hours of struggling with MS Word's "automated" features such as auto-bullets, auto-numbering, auto-indentation etc.
======================
The Design Should:
======================
- Be a Microsoft Word document, produced with Office 2013 or Office 365.
- Be suitable for production of printed manuals and online PDF manuals.
- Include the following sections:
1) Cover Page.
2) Approx 120 words of "warning text" (may be on cover or separate page).
3) Table Of Contents.
4) Body.
5) Specifications section featuring 3-10 different versions of the machine, each including a photo and listing approx 13 specifications.
- Include page numbers.
- Be in "Single Column Format" for easy editing by staff with minimal MS Word experience. "Special Pages", such as the cover and table of contents may be multi-column if necessary.
- Be an A4 document.
- Be readable when printed in Black and White, even if elements of the design include colour.
- Feature a warning icon/graphic that is easy to paste/insert next to important text.
- Feature the following levels of text, to be entered into MS Word's "Styles" function:
1) Main Headings.
2) Sub Headings.
3) Body Text.
- Feature headings that are "text", so they can be edited within MS Word without resorting to graphic editing software etc.
- Not rely on MS Word's painful "automated" features like auto-bullets, auto-numbering, auto-indentation etc (with the exception of page numbers, headings and auto-generated table of contents)
======================
How Our Staff Will Use It:
======================
Staff will have a basic understanding of MS Word.
Our staff will paste text, photographs, diagrams and vector drawings into the template.
======================
Extra Credit Given For:
======================
- Automatically generated table of contents, based on the headings within the document.
======================
Finished Template:
======================
- Should be in MS Word (MS Office 2013 or MS Office 365) format.
- Should include generic text / photos / diagrams to show what a manual looks like when generated from your template.
Project Deadline Extended
Reason: Following feedback, payment has been "committed".
Deadline extended to allow designers adequate time for production.

```html
<!DOCTYPE html>
<html lang="en">
<head>
<meta charset="utf-8">
<title>Instruction Manual for Consumer Machinery</title>
<link href="https://fonts.googleapis.com/css2?family=Roboto+Condensed:wght@400;700&display=swap" rel="stylesheet">
<style>
  :root {
    --brand-blue: #0a72b9;
    --title-blue: #0b74bd;
    --logo-blue: #6db3f2;
    --deep-blue: #003399;
    --amber: #f8a31c;
    --orange: #ff7000;
    --white: #ffffff;
    --frame: #3d4a78;
    --photo-top: #dfe6e4;
    --photo-bottom: #b9c4c2;
  }
  * { margin: 0; padding: 0; box-sizing: border-box; }
  html, body { width: 927px; height: 1200px; overflow: hidden; background: var(--white); }
  .cover {
    position: relative;
    width: 927px;
    height: 1200px;
    overflow: hidden;
    background: var(--white);
    font-family: "Roboto Condensed", "Arial Narrow", sans-serif;
  }
  .logo-badge {
    position: absolute;
    left: 738px; top: 55px;
    width: 145px; height: 145px;
    border-radius: 50%;
    background: var(--logo-blue);
    color: var(--white);
    display: flex; flex-direction: column; align-items: center; justify-content: center;
    text-align: center;
  }
  .logo-badge .logo-name { font-size: 35px; font-weight: 700; line-height: 1; }
  .logo-badge .logo-tag { font-size: 24px; font-weight: 400; line-height: 1.3; margin-top: 4px; }
  .title-intro {
    position: absolute;
    left: 65px; top: 354px;
    font-size: 39px; font-weight: 400;
    color: var(--title-blue);
    line-height: 1;
  }
  .title-band {
    position: absolute;
    left: 0; top: 401px;
    width: 622px; height: 68px;
    background: var(--brand-blue);
    display: flex; align-items: center;
    padding-left: 65px;
  }
  .title-band h1 {
    color: var(--white);
    font-size: 45px; font-weight: 700;
    letter-spacing: 2px;
    line-height: 1;
  }
  .waves { position: absolute; left: 0; top: 0; width: 927px; height: 1200px; }
  .product-frame {
    position: absolute;
    left: 597px; top: 567px;
    width: 305px; height: 449px;
    background: var(--white);
    border: 1px solid var(--frame);
    padding: 40px 40px 20px 30px;
  }
  .product-photo {
    width: 100%; height: 100%;
    background: linear-gradient(180deg, var(--photo-top), var(--photo-bottom));
  }
  .website {
    position: absolute;
    right: 49px; top: 1128px;
    color: var(--white);
    font-size: 26px; font-weight: 400;
  }
</style>
</head>
<body>
  <main class="cover">
    <svg class="waves" viewBox="0 0 850 1100" preserveAspectRatio="none" aria-hidden="true">
      <path d="M0 850 C150 855 360 880 580 945 L0 945 Z" fill="var(--amber)"/>
      <path d="M380 905 C550 880 700 855 850 830 L850 965 L380 965 Z" fill="var(--orange)"/>
      <path d="M0 942 C150 925 300 928 450 940 C600 952 750 956 850 950 L850 1100 L0 1100 Z" fill="var(--deep-blue)" stroke="#000" stroke-width="1.5"/>
    </svg>

    <div class="logo-badge">
      <span class="logo-name">Logo</span>
      <span class="logo-tag">Text Here</span>
    </div>

    <p class="title-intro">Instruction Manual for</p>
    <div class="title-band"><h1>CONSUMER MACHINERY</h1></div>

    <figure class="product-frame">
      <div class="product-photo" role="img" aria-label="Product photo: two-door glass-fronted fermentation cabinet with wire shelves"></div>
    </figure>

    <p class="website">www.yoursitetext.com</p>
  </main>
</body>
</html>
```